Business Card That Looks Like a Sports Card

Want it to look like a sports trading card. That front should have a baseball player. The back will list our contact info and website info etc.

Contact Information for Business Card

www.ridgecrestathletics.example
visitRCX.example
Email: marcus@ridgecrestathletics.example

Colors

Designer to choose colors to be used in the design.

Requirements
Must have
• Use our current logo and color scheme. Must look like a sports trading card.

```html
<!DOCTYPE html>
<html lang="en">
<head>
<meta charset="utf-8">
<title>Ridgecrest Athletics – Trading Card Business Card</title>
<link rel="stylesheet" href="https://fonts.googleapis.com/css2?family=Montserrat:wght@400;500;700&display=swap">
<style>
  :root {
    --navy: #0f1645;
    --grey: #b7cccd;
    --white: #ffffff;
    --paper: #f6f8f7;
    --green: #0dfc72;
    --stage: #e8ecec;
  }
  * { margin: 0; padding: 0; box-sizing: border-box; }
  html, body { width: 1200px; height: 829px; overflow: hidden; }
  body {
    background: var(--stage);
    font-family: "Montserrat", Arial, sans-serif;
    color: var(--navy);
    position: relative;
  }
  .card {
    position: absolute;
    top: 101px;
    width: 448px;
    height: 627px;
    overflow: hidden;
  }
  .card--front { left: 126px; }
  .card--back { left: 626px; }
  .card__frame { position: absolute; inset: 0; display: block; }

  /* front */
  .brand-mark {
    position: absolute;
    left: 54px; top: 76px;
    width: 120px;
    text-align: center;
    font-weight: 700;
    font-size: 15px;
    line-height: 1.2;
    letter-spacing: 0.5px;
    text-transform: uppercase;
    color: var(--navy);
  }
  .player-photo {
    position: absolute;
    left: 178px; top: 40px;
    width: 160px; height: 555px;
    border-radius: 60px 60px 20px 20px;
    background: linear-gradient(180deg, #2f5a35 0%, #2a5330 45%, #dfe5e2 58%, #d6dcda 88%, #2e4d33 100%);
  }
  .title-plate {
    position: absolute;
    left: 140px; right: 0; top: 451px;
    height: 62px;
    background: var(--navy);
    border-radius: 12px 0 0 12px;
    box-shadow: 0 3px 0 var(--grey);
    display: flex; align-items: center; justify-content: flex-end;
    padding-right: 18px;
  }
  .title-plate__text {
    color: var(--white);
    font-weight: 700;
    font-size: 33px;
  }
  .title-strip {
    position: absolute;
    left: 173px; right: 0; top: 517px;
    height: 31px;
    background: var(--green);
    border-radius: 10px 0 0 10px;
    display: flex; align-items: center; justify-content: flex-end;
    padding-right: 8px;
  }
  .title-strip__text {
    color: var(--white);
    font-size: 15px;
    letter-spacing: -0.6px;
  }

  /* back */
  .back-mark {
    position: absolute;
    left: 40px; right: 40px; top: 125px;
    text-align: center;
    font-weight: 700;
    font-size: 42px;
    line-height: 1.1;
    letter-spacing: 2px;
    text-transform: uppercase;
    color: var(--navy);
  }
  .about {
    position: absolute;
    left: 30px; right: 30px; top: 323px;
    text-align: center;
    font-size: 12.3px;
    line-height: 16.3px;
  }
  .contact-heading {
    position: absolute;
    left: 119px; top: 445px;
    width: 201px; height: 26px;
    background: var(--navy);
    color: var(--white);
    border-radius: 3px;
    font-size: 16px;
    font-weight: 500;
    text-align: center;
    line-height: 26px;
  }
  .contact-list {
    position: absolute;
    left: 20px; right: 20px; top: 482px;
    list-style: none;
    text-align: center;
  }
  .contact-list li {
    height: 28px;
    display: flex; align-items: center; justify-content: center;
    gap: 4px;
    font-size: 15.5px;
    font-weight: 500;
  }
  .contact-list svg { width: 20px; height: 20px; flex: none; }
</style>
</head>
<body>

<section class="card card--front" aria-label="Card front">
  <svg class="card__frame" viewBox="0 0 448 627" aria-hidden="true">
    <rect width="448" height="627" fill="var(--navy)"/>
    <rect x="0" y="440" width="448" height="187" fill="var(--green)"/>
    <path d="M170 21 H448 V420 A184 184 0 0 1 264 604 H0 V191 A170 170 0 0 1 170 21 Z" fill="var(--grey)"/>
    <path d="M171 21 H425 V430 A170 170 0 0 1 255 600 H21 V171 A150 150 0 0 1 171 21 Z" fill="var(--paper)"/>
  </svg>
  <div class="player-photo" role="img" aria-label="Photo of a baseball player in a green jersey and white pants holding a glove"></div>
  <div class="brand-mark">Ridgecrest<br>Athletics</div>
  <div class="title-plate"><span class="title-plate__text">Baseball Player</span></div>
  <div class="title-strip"><span class="title-strip__text">jerseys, helmets, shoes, bats and balls</span></div>
</section>

<section class="card card--back" aria-label="Card back">
  <svg class="card__frame" viewBox="0 0 448 627" aria-hidden="true">
    <g transform="translate(448 0) scale(-1 1)">
      <rect width="448" height="627" fill="var(--navy)"/>
      <rect x="0" y="440" width="448" height="187" fill="var(--green)"/>
      <path d="M170 21 H448 V420 A184 184 0 0 1 264 604 H0 V191 A170 170 0 0 1 170 21 Z" fill="var(--grey)"/>
      <path d="M171 21 H425 V430 A170 170 0 0 1 255 600 H21 V171 A150 150 0 0 1 171 21 Z" fill="var(--white)"/>
    </g>
  </svg>
  <div class="back-mark">Ridgecrest<br>Athletics</div>
  <p class="about">The best in game used and autographed sports memorabilia from our favorite teams in the Midwest and beyond. Game worn jerseys, helmets, shoes, bats and balls that saw real game action from All-Stars and Hall of Famers! Autographs and memorabilia directly from pro football, pro basketball, pro baseball and the soccer pitch.</p>
  <div class="contact-heading">Contact Information</div>
  <ul class="contact-list">
    <li>
      <svg viewBox="0 0 20 20" fill="none" stroke="var(--navy)" stroke-width="1.4" aria-hidden="true"><circle cx="10" cy="10" r="8.5"/><ellipse cx="10" cy="10" rx="3.8" ry="8.5"/><path d="M1.5 10h17M3 5.5h14M3 14.5h14"/></svg>
      <span>www.ridgecrestathletics.example</span>
    </li>
    <li>
      <svg viewBox="0 0 20 20" fill="none" stroke="var(--navy)" stroke-width="1.4" aria-hidden="true"><circle cx="10" cy="10" r="8.5"/><ellipse cx="10" cy="10" rx="3.8" ry="8.5"/><path d="M1.5 10h17M3 5.5h14M3 14.5h14"/></svg>
      <span>visitRCX.example</span>
    </li>
    <li>
      <svg viewBox="0 0 20 20" fill="none" stroke="var(--navy)" stroke-width="1.4" aria-hidden="true"><rect x="1.5" y="4" width="17" height="12"/><path d="M1.5 4l8.5 7 8.5-7M1.5 16l6-5.5M18.5 16l-6-5.5"/></svg>
      <span>marcus@ridgecrestathletics.example</span>
    </li>
  </ul>
</section>

</body>
</html>
```